Business Card Design Project

Recently had a new logo made up for my company and new business cards done as well. I have attached the logos for your viewing. Additional projects may be needed. Good luck!

Industry/Entity Type

Business

```html
<!DOCTYPE html>
<html lang="en">
<head>
<meta charset="utf-8">
<title>Hartwell Financial Group – Business Card</title>
<link rel="stylesheet" href="https://fonts.googleapis.com/css2?family=Lato:wght@400;700&display=swap">
<style>
  :root {
    --canvas: #ffffff;
    --frame: #c8c8c8;
    --card: #23232b;
    --gold: #c9b383;
    --light: #f2f2f2;
  }
  * { margin: 0; padding: 0; box-sizing: border-box; }
  html, body {
    width: 1200px; height: 900px; overflow: hidden;
    background: var(--canvas);
    font-family: "Lato", "Helvetica Neue", Arial, sans-serif;
  }
  .sheet {
    position: relative; width: 1200px; height: 900px;
    border: 1px solid var(--frame);
  }
  .card {
    position: absolute; left: 233px; width: 735px; height: 422px;
    background: var(--card);
  }
  .card--front { top: 17px; }
  .card--back { top: 457px; }

  .brand {
    position: absolute;
    color: var(--gold); font-size: 22px; font-weight: 400;
    line-height: 1; white-space: nowrap;
  }
  .card--front .brand { left: 44px; top: 110px; }
  .card--back .brand { left: 0; right: 0; top: 168px; text-align: center; font-size: 26px; }

  .person { position: absolute; left: 327px; top: 154px; color: var(--gold); }
  .person__name { font-size: 31px; font-weight: 400; line-height: 1.1; }
  .person__title { font-size: 18.5px; margin-top: 4px; }

  .contacts {
    position: absolute; left: 326px; top: 270px; list-style: none;
  }
  .contacts__item {
    display: flex; align-items: center; height: 29.5px;
    color: var(--light); font-size: 21px;
  }
  .contacts__icon { width: 23px; height: 23px; margin-right: 10px; flex: none; }

  .address {
    position: absolute; left: 0; right: 0; top: 362px;
    text-align: center; color: var(--light); font-size: 18.5px;
  }
</style>
</head>
<body>
<div class="sheet">

  <section class="card card--front">
    <p class="brand">Hartwell Financial Group</p>

    <div class="person">
      <h1 class="person__name">Daniel R. Hartwell</h1>
      <p class="person__title">Estate Planning and Insurance Specialist</p>
    </div>

    <ul class="contacts">
      <li class="contacts__item">
        <svg class="contacts__icon" viewBox="0 0 24 24" aria-hidden="true">
          <circle cx="12" cy="12" r="12" fill="#c9b383"/>
          <rect x="5.5" y="7.5" width="13" height="9" fill="none" stroke="#23232b" stroke-width="1.6"/>
          <path d="M5.5 7.5 L12 13 L18.5 7.5 M5.5 16.5 L10 12 M18.5 16.5 L14 12" fill="none" stroke="#23232b" stroke-width="1.4"/>
        </svg>
        Dhartwell@hartwellfinancial.com
      </li>
      <li class="contacts__item">
        <svg class="contacts__icon" viewBox="0 0 24 24" aria-hidden="true">
          <circle cx="12" cy="12" r="12" fill="#c9b383"/>
          <path d="M8.3 5.5 L10.3 8.8 L8.8 10.2 Q10.2 13.3 13.6 15.1 L15 13.6 L18.4 15.6 L17 18.4 Q10.5 18.5 6 10 Q6 7 8.3 5.5 Z" fill="#23232b"/>
        </svg>
        516-555-0148
      </li>
      <li class="contacts__item">
        <svg class="contacts__icon" viewBox="0 0 24 24" aria-hidden="true">
          <circle cx="12" cy="12" r="12" fill="#c9b383"/>
          <rect x="8" y="5" width="8" height="5" fill="#23232b"/>
          <rect x="5.5" y="10" width="13" height="6" rx="1" fill="#23232b"/>
          <rect x="8" y="14" width="8" height="5" fill="#c9b383" stroke="#23232b" stroke-width="1.2"/>
        </svg>
        516-555-0192
      </li>
      <li class="contacts__item">
        <svg class="contacts__icon" viewBox="0 0 24 24" aria-hidden="true">
          <circle cx="12" cy="12" r="12" fill="#c9b383"/>
          <g fill="none" stroke="#23232b" stroke-width="1.3">
            <circle cx="12" cy="12" r="6.5"/>
            <ellipse cx="12" cy="12" rx="3" ry="6.5"/>
            <path d="M5.5 12 H18.5 M6.5 9 H17.5 M6.5 15 H17.5"/>
          </g>
        </svg>
        www.hartwellfinancial.com
      </li>
    </ul>
  </section>

  <section class="card card--back">
    <p class="brand">Hartwell Financial Group</p>
    <p class="address">4200 Meadow Crest Road, Suite 310E, Lindenhurst, New York 11757</p>
  </section>

</div>
</body>
</html>
```